Simple but strong message business card.

I will be using this to communicate a message about how we are different from our main competitor. I will be giving these out at a trade show. It needs to have our logo and then communicate that we do not charge PCI Fees. Our competitor charges junk fees at an exorbitant amount and our target audience is aware of it and tired of the BS.

Target Market(s)

Attendees of a trade show. General managers of the ridgeline growers union. www.fieldhallmark.net

Contact Information for Business Card

Font styles to use
Sans Serif

Colors

Designer to choose colors to be used in the design.

Requirements
Must have
• Our logo. and the message of No PCI Fees
• contact email - tbrolin@quillmerchant.net
• contact name - Dane Brolin
• contact phone - 303-555-0142

```html
<!DOCTYPE html>
<html lang="en">
<head>
<meta charset="utf-8">
<title>Quill Merchant Business Card</title>
<link href="https://fonts.googleapis.com/css2?family=Open+Sans:wght@400;600;700&display=swap" rel="stylesheet">
<style>
  :root {
    --backdrop: #e9e6e1;
    --card-white: #ffffff;
    --slate: #616366;
    --brand-green: #72b043;
    --ink: #4a4a4a;
    --text-light: #ffffff;
  }
  * { margin: 0; padding: 0; box-sizing: border-box; }
  html, body { width: 1200px; height: 1000px; overflow: hidden; }
  body {
    background: var(--backdrop);
    font-family: "Open Sans", Arial, sans-serif;
    position: relative;
  }
  .card {
    position: absolute;
    width: 666px;
    height: 397px;
    border-radius: 22px;
    background: var(--card-white);
    overflow: hidden;
    box-shadow: 0 6px 14px rgba(0,0,0,0.25);
  }
  .card--front { left: 262px; top: 74px; }
  .card--back { left: 266px; top: 533px; }
  .front-shapes { position: absolute; inset: 0; }
  .wordmark {
    position: absolute;
    display: flex;
    align-items: center;
    gap: 10px;
    color: var(--brand-green);
    font-weight: 700;
    letter-spacing: 0.5px;
    white-space: nowrap;
  }
  .wordmark__dot {
    border-radius: 50%;
    background: var(--brand-green);
    flex: none;
  }
  .card--front .wordmark { left: 34px; top: 184px; font-size: 25px; }
  .card--front .wordmark__dot { width: 24px; height: 24px; }
  .card--back .wordmark { left: 0; right: 0; top: 165px; justify-content: center; font-size: 42px; gap: 12px; }
  .card--back .wordmark__dot { width: 40px; height: 40px; }
  .contact {
    position: absolute;
    right: 32px;
    top: 92px;
    text-align: right;
    color: var(--text-light);
    font-size: 16px;
    line-height: 23px;
  }
  .contact__name { color: var(--brand-green); font-size: 24px; font-weight: 700; line-height: 30px; }
  .contact__title { margin-bottom: 40px; }
  .contact__address { margin-bottom: 16px; }
  .contact__line { display: flex; justify-content: flex-end; align-items: center; gap: 5px; line-height: 24px; }
  .contact__line svg { width: 14px; height: 14px; flex: none; }
  .accent { color: var(--brand-green); }
  .tagline {
    position: absolute;
    left: 0; right: 0;
    top: 340px;
    text-align: center;
    color: var(--ink);
    font-size: 20px;
  }
</style>
</head>
<body>
  <section class="card card--front">
    <svg class="front-shapes" viewBox="0 0 666 397" width="666" height="397" aria-hidden="true">
      <path d="M158 -4 C 385 70 437 290 256 401" fill="none" stroke="var(--brand-green)" stroke-width="24"/>
      <path d="M176 -4 C 405 68 460 300 276 401" fill="none" stroke="#ffffff" stroke-width="4"/>
      <path d="M178 -4 C 407 68 462 300 278 401 L670 401 L670 -4 Z" fill="var(--slate)"/>
    </svg>
    <div class="wordmark"><span class="wordmark__dot"></span><span>QUILL MERCHANT</span></div>
    <div class="contact">
      <div class="contact__name">Dane Brolin</div>
      <div class="contact__title">Chief Executive Officer</div>
      <div class="contact__address">418 W. Alder Street<br>Fenwick, Missouri 63920</div>
      <div class="contact__line"><span>303-555-0142</span>
        <svg viewBox="0 0 14 14"><rect x="4" y="1" width="6.5" height="12" rx="1.2" fill="none" stroke="var(--brand-green)" stroke-width="1.3"/></svg>
      </div>
      <div class="contact__line"><span>303-555-0187</span>
        <svg viewBox="0 0 14 14"><path d="M1 6 Q7 1 13 6 L11 7.5 L9 6 L5 6 L3 7.5 Z" fill="var(--brand-green)"/><rect x="3" y="8" width="8" height="4.5" rx="1" fill="var(--brand-green)"/></svg>
      </div>
      <div class="contact__line"><span>tbrolin@quillmerchant.net</span>
        <svg viewBox="0 0 14 14"><rect x="1" y="3" width="12" height="8.5" fill="var(--brand-green)"/><path d="M1 3 L7 8 L13 3" fill="none" stroke="var(--slate)" stroke-width="1"/></svg>
      </div>
      <div class="contact__line"><span>www.<span class="accent">quillmerchant</span>.net</span>
        <svg viewBox="0 0 14 14"><circle cx="6" cy="6" r="4.5" fill="none" stroke="var(--brand-green)" stroke-width="1.5"/><path d="M7 7 L13 9 L10.5 10 L12 13 L11 13.5 L9.5 10.6 L8 12.5 Z" fill="var(--brand-green)"/></svg>
      </div>
    </div>
  </section>

  <section class="card card--back">
    <div class="wordmark"><span class="wordmark__dot"></span><span>QUILL MERCHANT</span></div>
    <p class="tagline">No PCI Fees Required</p>
  </section>
</body>
</html>
```